This book will apply the 12 Steps to gaming addiction, also known as video game addiction. The primary purpose of the book is to provide an effective solution for this new type of addiction. The solution is based on the rich and successful concepts of traditional twelve-step programs like RL.

The title on the cover will be "Nine Doors Past the Glowing Screen" and "by Martin Quorby". A subtitle can be used if it works in your design of "A Practical Path Beyond Compulsive Console Play". Cover will be for a 6" x 9" book approximately 110 pages in length.

Some back cover text including some review quotes and an author bio are in the attached Word doc. There is also an author photo attached for for the back cover.

Requirements
Must have
• For the cover design it could be stylized, or an image, a partial image, or whatever. I am open to suggestions. Think about what would be noticed by a person searching for help with moderating their video game use, or by the parents or loved ones of problem gamers. Something contemporary and eye catching.

```html
<!DOCTYPE html>
<html lang="en">
<head>
<meta charset="utf-8">
<title>Nine Doors Past the Glowing Screen — Cover Wrap</title>
<link rel="stylesheet" href="https://fonts.googleapis.com/css2?family=Bebas+Neue&family=Vollkorn:ital,wght@0,400;0,600;1,400&display=swap">
<style>
  :root {
    --navy-deep: #2c3a78;
    --navy: #3a4a8c;
    --mist: #dfe3ee;
    --mist-light: #f3f4f8;
    --ink: #1f2a5c;
    --accent-red: #ee3b45;
    --quote-red: #c0182a;
    --rule: #1d3580;
    --gold: #efe08a;
    --white: #ffffff;
  }
  * { margin: 0; padding: 0; box-sizing: border-box; }
  html, body { width: 1200px; height: 888px; overflow: hidden; background: var(--navy-deep); }
  .cover-wrap {
    position: relative;
    width: 1200px; height: 888px; overflow: hidden;
    background:
      radial-gradient(ellipse 360px 520px at 930px 560px, var(--mist-light) 0%, var(--mist) 35%, rgba(200,206,226,0) 100%),
      radial-gradient(ellipse 520px 600px at 300px 420px, #c9cee2 0%, #9aa2c8 55%, rgba(90,102,160,0) 100%),
      linear-gradient(90deg, var(--navy) 0%, #7580b2 30%, #8e97c2 52%, #a8afd0 60%, #c6cbe0 75%, var(--navy-deep) 100%);
    font-family: "Vollkorn", Georgia, serif;
    color: var(--ink);
  }

  /* Back cover */
  .back-title {
    position: absolute; left: 35px; top: 40px; width: 530px;
    font-family: "Bebas Neue", "Oswald", sans-serif;
    font-size: 35px; letter-spacing: 2.4px; color: var(--white); line-height: 1;
    white-space: nowrap;
  }
  .reviews { position: absolute; left: 38px; top: 85px; width: 525px; }
  .review { font-size: 12.4px; line-height: 14.8px; margin-bottom: 16px; }
  .review-source { color: var(--quote-red); }
  .review-source b { font-weight: 600; }
  .review-source i { font-style: italic; }
  .back-rule { position: absolute; left: 32px; top: 350px; width: 533px; height: 2px; background: var(--rule); }
  .blurb { position: absolute; left: 38px; top: 366px; width: 525px; }
  .blurb p { font-size: 12.4px; line-height: 14.8px; margin-bottom: 14.5px; }
  .author-photo { position: absolute; left: 32px; top: 630px; width: 256px; height: 234px; }
  .author-bio {
    position: absolute; left: 306px; top: 626px; width: 250px;
    font-style: italic; font-size: 10.4px; line-height: 13px;
  }
  .barcode-space { position: absolute; left: 370px; top: 746px; width: 196px; height: 118px; background: var(--white); }

  /* Spine */
  .spine-title, .spine-author {
    position: absolute; left: 604px;
    font-family: "Bebas Neue", "Oswald", sans-serif;
    font-size: 15px; letter-spacing: 1.4px; color: var(--ink);
    writing-mode: vertical-rl; white-space: nowrap;
  }
  .spine-title { top: 48px; }
  .spine-author { top: 738px; color: var(--white); }

  /* Front cover */
  .front-title {
    position: absolute; left: 648px; top: 40px; width: 532px;
    font-family: "Bebas Neue", "Oswald", sans-serif; line-height: 1; text-align: center;
  }
  .front-title .line-white {
    display: block; font-size: 70px; letter-spacing: 1px; color: var(--white);
    text-shadow: 2px 3px 0 rgba(40,50,100,0.55);
  }
  .front-title .line-red {
    display: block; margin-top: 10px; font-size: 72px; letter-spacing: 1px; color: var(--accent-red);
  }
  .subtitle {
    position: absolute; left: 648px; top: 215px; width: 532px; text-align: center;
    font-size: 20px; letter-spacing: 0.3px; color: var(--navy-deep);
  }
  .cover-photo { position: absolute; left: 704px; top: 256px; width: 496px; height: 632px; }
  .front-author {
    position: absolute; left: 732px; top: 800px;
    font-size: 46px; font-weight: 600; color: var(--gold); letter-spacing: 0.5px;
    text-shadow: 1px 2px 2px rgba(0,0,0,0.35);
  }
</style>
</head>
<body>
<main class="cover-wrap">
  <section class="back-cover">
    <h2 class="back-title">Nine Doors Past the Glowing Screen</h2>
    <div class="reviews">
      <p class="review">“A must-read for anyone who is addicted to or thinks they may have a problem with digital gaming. This eloquent work will also be useful to academics and clinicians exploring potential solutions. The author recognizes the similarities between gaming addiction and other addictions, and logically applies one of the most effective known solutions for addiction - The Twelve Steps.”<br><span class="review-source">-- <b>Dale Warrington,</b> <i>Noted Interventionist and Keynote Speaker.</i></span></p>
      <p class="review">“If you suffer from digital gaming addiction, I strongly encourage you to use this book as your road map to get you back to the real world.”<br><span class="review-source">-- <b>Peter Vantolle,</b> <i>Founder of Network Habits Review.</i></span></p>
      <p class="review">“As a high school teacher for 24 years, husband, father, coach, and 12-Step member, I can assure you that this book will transform the life of anyone who is addicted to video games. Well written, easy to understand, and a wonderful book that will provide you with a clear road map to recovery, and this includes teenagers, a group I have been working with in the classroom for decades.”<br><span class="review-source">-- <b>Lucas Ferrante, Harbor Point,</b> <i>CA High School Teacher.</i></span></p>
    </div>
    <div class="back-rule"></div>
    <div class="blurb">
      <p>An effective solution to the challenge of Digital Gaming Addiction (aka Video Game Addiction) based on the rich and successful tradition of the Twelve Steps.</p>
      <p>Addiction to Digital Gaming is a new and troubling phenomenon that has burst upon an unprepared society with alarming speed. Many people crave the use of Digital Games in a strikingly similar way to any other addict. Digital Games are a complex software and hardware system that have been designed to promote continued and progressive usage. This sophisticated technology clearly feeds on natural addictive tendencies.</p>
      <p>The 12 Steps are one of the most effective methods for treating addiction in human history. Originating with Restoration League in 1939, the 12 Steps have since been used to treat a variety of other addictions, including drugs, sex, gambling, eating disorders, and many others. Now in this groundbreaking work the 12 Steps are applied to the complex and evolving contemporary phenomenon of Digital Gaming Addiction.</p>
    </div>
    <svg class="author-photo" viewBox="0 0 256 234" role="img" aria-label="Author portrait photo: smiling man in a dark jacket in front of green foliage">
      <defs>
        <linearGradient id="authorPhotoTone" x1="0" y1="0" x2="0" y2="1">
          <stop offset="0" stop-color="#7f8f4a"/>
          <stop offset="0.55" stop-color="#5d6a3a"/>
          <stop offset="1" stop-color="#23283a"/>
        </linearGradient>
      </defs>
      <rect width="256" height="234" fill="url(#authorPhotoTone)"/>
    </svg>
    <p class="author-bio">Marty Quorby is a Technology Consultant and Writer with many years of professional coding and consulting experience. He also struggled with addiction to drugs and alcohol and is now clean and sober in a Twelve-Step program for over 17 years. This unique combination of 12-Step experience and technology expertise led him to create Nine Doors Past the Glowing Screen.</p>
    <div class="barcode-space"></div>
  </section>

  <section class="spine">
    <span class="spine-title">Nine Doors Past the Glowing Screen</span>
    <span class="spine-author">By Martin Quorby</span>
  </section>

  <section class="front-cover">
    <svg class="cover-photo" viewBox="0 0 496 632" role="img" aria-label="Photo of a determined young blond man gripping a game controller">
      <defs>
        <radialGradient id="coverPhotoTone" cx="0.45" cy="0.4" r="0.7">
          <stop offset="0" stop-color="#e3c0a6" stop-opacity="0.85"/>
          <stop offset="0.45" stop-color="#b89a86" stop-opacity="0.6"/>
          <stop offset="1" stop-color="#3f4b7c" stop-opacity="0.85"/>
        </radialGradient>
      </defs>
      <rect width="496" height="632" fill="url(#coverPhotoTone)"/>
    </svg>
    <h1 class="front-title">
      <span class="line-white">NINE DOORS PAST THE</span>
      <span class="line-red">GLOWING SCREEN</span>
    </h1>
    <p class="subtitle">A Practical Path Beyond Compulsive Console Play</p>
    <p class="front-author">by Martin Quorby</p>
  </section>
</main>
</body>
</html>
```